We require a professional design for a Cosmetic Surgery college. We have just submitted the request for our new logo which will be used on this card. We are the leaders in our field of education in Australia and this should be reflected in the quality of the card. People want to come and study with us because we are so outstanding in the field. Studying with us provides credibility, quality and courage.
Updates

Project Deadline Extended
Reason: Require updated logo to be used in design

Target Market(s)

25 - 40 year old professional women primarily from a medical background wanting to continue study in the cosmetic medical field, western speaking countries. The course average cost is 17k AU for 16 weeks.

Industry/Entity Type

Education

Requirements
Must have
• Must us the logo that is currently under design by this company.
Nice to have
• A medical twist very subtle would be nice possilbly rod of Asclepius.
Should not have
• Should not look old, we are dealing with modern medical concepts.
The logo that is being redesigned 3d silver, the attached logo is the old one.

```html
<!DOCTYPE html>
<html lang="en">
<head>
<meta charset="utf-8">
<title>Ashvale Business Card</title>
<link href="https://fonts.googleapis.com/css2?family=Open+Sans:wght@400;600&display=swap" rel="stylesheet">
<style>
  :root {
    --stage: #3a3a3a;
    --card-dark: #231f20;
    --card-light: #ffffff;
    --silver: #b9b9b9;
    --silver-dark: #8c8c8c;
    --ink: #231f20;
    --band: #231f20;
    --band-text: #ffffff;
    --swoosh: #7a7a7a;
  }
  * { margin: 0; padding: 0; box-sizing: border-box; }
  html, body {
    width: 1200px; height: 750px; overflow: hidden;
    background: var(--stage);
    font-family: "Open Sans", Arial, sans-serif;
  }
  .stage { position: relative; width: 1200px; height: 750px; }
  .card {
    position: absolute; top: 211px; width: 511px; height: 292px;
    border-radius: 22px; overflow: hidden;
    box-shadow: 0 4px 12px rgba(0,0,0,0.45);
  }
  .card-front { left: 78px; background: var(--card-dark); }
  .card-back { left: 609px; background: var(--card-light); }

  .brand {
    position: absolute; display: flex; align-items: center; gap: 14px;
    font-weight: 600; letter-spacing: 2px;
  }
  .brand-dot { border-radius: 50%; flex: none; }
  .card-front .brand { left: 72px; top: 180px; font-size: 46px; color: var(--silver); line-height: 1; }
  .card-front .brand-dot { width: 58px; height: 58px; background: var(--silver); }
  .card-back .brand { left: 0; right: 0; justify-content: center; top: 40px; font-size: 38px; color: var(--silver-dark); line-height: 1; }
  .card-back .brand-dot { width: 48px; height: 48px; background: var(--silver-dark); }

  .rule { position: absolute; left: 0; right: 0; height: 1px; background: var(--band); }
  .rule-top { top: 114px; }
  .rule-bottom { top: 161px; }
  .name-band {
    position: absolute; left: 0; right: 0; top: 119px; height: 39px;
    background: var(--band); color: var(--band-text);
    display: flex; align-items: center; padding-left: 27px;
  }
  .name { font-size: 21px; }
  .divider { width: 1px; height: 22px; background: var(--band-text); margin: 0 8px; }
  .designation { font-size: 14px; }

  .contact-list { position: absolute; left: 27px; top: 173px; list-style: none; }
  .contact-list li {
    display: flex; align-items: center; gap: 13px;
    font-size: 14px; color: var(--ink); height: 17.5px;
  }
  .contact-list svg { width: 11px; height: 11px; fill: var(--ink); flex: none; }

  .address {
    position: absolute; right: 32px; top: 174px;
    font-size: 14px; color: var(--ink); text-align: right; line-height: 19px;
  }
  .address .pin { position: absolute; right: -18px; top: 3px; width: 11px; height: 14px; fill: var(--ink); }

  .wave { position: absolute; left: 0; bottom: 0; width: 511px; height: 60px; }
</style>
</head>
<body>
<main class="stage">
  <section class="card card-front" aria-label="Card front">
    <div class="brand"><span class="brand-dot"></span><span class="brand-name">ASHVALE</span></div>
  </section>

  <section class="card card-back" aria-label="Card back">
    <div class="brand"><span class="brand-dot"></span><span class="brand-name">ASHVALE</span></div>

    <div class="rule rule-top"></div>
    <div class="name-band">
      <span class="name">your name</span><span class="divider"></span><span class="designation">designation</span>
    </div>
    <div class="rule rule-bottom"></div>

    <ul class="contact-list">
      <li><svg viewBox="0 0 12 12"><path d="M1 4c0-2 2-3 5-3s5 1 5 3l-2 1-1-1H4L3 5zM2 6h8l1 5H1z"/></svg>0123 456 789</li>
      <li><svg viewBox="0 0 12 12"><path d="M3 0h6v12H3zM4 1v9h4V1z"/></svg>0123 456 789</li>
      <li><svg viewBox="0 0 12 12"><path d="M0 2h12v8H0zM1 3l5 4 5-4z"/></svg>youremail@mail.com</li>
      <li><svg viewBox="0 0 12 12"><path d="M6 0a6 6 0 1 0 0 12A6 6 0 0 0 6 0zm0 1c1 1 1.5 3 1.5 5S7 10 6 11C5 10 4.5 8 4.5 6S5 2 6 1zM1 5.5h10v1H1z"/></svg>www.yourwebsite.com</li>
    </ul>

    <address class="address" style="font-style:normal">
      address (street address<br>suite number, city, state, zip
      <svg class="pin" viewBox="0 0 10 14"><path d="M5 0a5 5 0 0 0-5 5c0 4 5 9 5 9s5-5 5-9a5 5 0 0 0-5-5zm0 3a2 2 0 1 1 0 4 2 2 0 0 1 0-4z"/></svg>
    </address>

    <svg class="wave" viewBox="0 0 511 60" preserveAspectRatio="none" aria-hidden="true">
      <path d="M0 20 C120 50 300 50 511 0 L511 8 C320 50 150 55 0 30 Z" fill="var(--swoosh)"/>
      <path d="M0 28 C150 60 320 55 511 12 L511 60 L0 60 Z" fill="var(--band)"/>
      <path d="M160 40 C300 45 420 30 511 10 L511 14 C420 36 300 48 160 40 Z" fill="#ffffff"/>
    </svg>
  </section>
</main>
</body>
</html>
```